Business Card Design

We need a business card designed to portray the message that we are wedding and event stylists. We set up garden ceremonies and style wedding reception venues with chair covers and sashes, backdrops and draping's, wishing wells, tealight holders, table centerpieces. We also style corporate functions - Christmas parties, gala dinners, school formals, award nights. The colour of our uniforms are black and hot pink, if these colours could be incorporated. We would like to be able to use this design for letterhead, flyers and postcards etc. We would like the design to portray a professional, classic image that would relate to both spectrums of our business, weddings and corporate events. If you could develop a logo to incorporate would be great

Target Market(s)

brides, corporate compaines

Industry/Entity Type

Wedding

Contact Information for Business Card

Velvet Crest Occasions & Party Hire
Phone: 0417 553 916 Email:vcoph@fernmail.example
Web: www.velvetcrestoccasions.example.au

Requirements
Must have
• Must include that we set up for weddings, engagements, birthdays, anniversaries, corporate functions, school formals, any occasion.

```html
<!DOCTYPE html>
<html lang="en">
<head>
<meta charset="utf-8">
<title>Velvet Crest Occasions – Business Card</title>
<link rel="stylesheet" href="https://fonts.googleapis.com/css2?family=Questrial&display=swap">
<style>
  :root {
    --page: #ffffff;
    --card-cream: #f4e8d6;
    --damask: #e6d2b4;
    --brown: #4a2e1c;
    --ink: #2b2018;
    --gold: #c58f2c;
    --gold-light: #e6c27a;
    --gold-deep: #a8741c;
    --photo-dark: #3b3533;
    --photo-mid: #9d9690;
    --photo-light: #e9e5df;
  }
  * { margin: 0; padding: 0; box-sizing: border-box; }
  html, body {
    width: 1200px;
    height: 900px;
    overflow: hidden;
    background: var(--page);
    font-family: "Questrial", "Century Gothic", sans-serif;
  }
  .business-card {
    position: absolute;
    left: 60px;
    top: 118px;
    width: 1080px;
    height: 663px;
    overflow: hidden;
    background: var(--card-cream);
  }
  .card-texture {
    position: absolute;
    inset: 0;
    background:
      radial-gradient(ellipse at 20% 30%, var(--damask) 0%, transparent 55%),
      radial-gradient(ellipse at 70% 80%, var(--damask) 0%, transparent 50%),
      linear-gradient(135deg, var(--card-cream), #efdfc6);
  }
  .card-art {
    position: absolute;
    inset: 0;
    width: 1080px;
    height: 663px;
  }
  .brand-name {
    position: absolute;
    left: 40px;
    top: 64px;
    width: 560px;
    text-align: center;
    color: var(--brown);
    font-size: 58px;
    line-height: 60px;
  }
  .services {
    position: absolute;
    left: 40px;
    top: 246px;
    width: 560px;
    text-align: center;
    color: var(--gold);
    font-size: 20px;
    line-height: 27px;
  }
  .contact-person {
    position: absolute;
    left: 64px;
    top: 420px;
  }
  .person-name {
    color: var(--ink);
    font-size: 29px;
    line-height: 34px;
  }
  .person-role {
    color: var(--gold);
    font-size: 20px;
    line-height: 26px;
  }
  .contact-list {
    position: absolute;
    left: 62px;
    top: 494px;
    list-style: none;
  }
  .contact-list li {
    display: flex;
    align-items: center;
    gap: 10px;
    height: 36px;
    color: var(--ink);
    font-size: 28px;
  }
  .contact-list svg {
    width: 28px;
    height: 28px;
    flex: none;
  }
</style>
</head>
<body>
  <section class="business-card">
    <div class="card-texture" role="img" aria-label="Soft cream damask background pattern"></div>

    <svg class="card-art" viewBox="0 0 1080 663" aria-hidden="false">
      <defs>
        <linearGradient id="gold-band" x1="0" y1="0" x2="0" y2="1">
          <stop offset="0" stop-color="var(--gold-light)"/>
          <stop offset="0.5" stop-color="var(--gold)"/>
          <stop offset="1" stop-color="var(--gold-deep)"/>
        </linearGradient>
        <linearGradient id="venue-photo" x1="0" y1="0" x2="0" y2="1">
          <stop offset="0" stop-color="var(--photo-dark)"/>
          <stop offset="0.35" stop-color="var(--photo-mid)"/>
          <stop offset="0.7" stop-color="var(--photo-light)"/>
          <stop offset="1" stop-color="#d8d2ca"/>
        </linearGradient>
      </defs>
      <path class="gold-crescent" fill="url(#gold-band)"
            d="M612 0 C552 220 580 470 752 663 L772 663 C604 452 594 205 642 0 Z"/>
      <path class="venue-photo" fill="url(#venue-photo)" role="img"
            aria-label="Photo of a styled reception table with a tall glass vase centrepiece of white orchids and tealight candles"
            d="M642 0 C594 205 604 452 772 663 L1080 663 L1080 0 Z"/>
    </svg>

    <h1 class="brand-name">Velvet Crest<br>Occasions</h1>

    <p class="services">
      Offering the complete event and styling solution from<br>
      concept to completion<br>
      Weddings | Engagements | Birthdays | Anniversaries<br>
      | School Formals |<br>
      Corporate Functions | Any Occasion
    </p>

    <div class="contact-person">
      <p class="person-name">Lorena Haske</p>
      <p class="person-role">Event Designer</p>
    </div>

    <ul class="contact-list">
      <li>
        <svg viewBox="0 0 24 24" aria-label="Phone"><path fill="var(--gold)" d="M6.6 10.8a15 15 0 0 0 6.6 6.6l2.2-2.2c.3-.3.7-.4 1-.2 1.1.4 2.3.6 3.6.6.6 0 1 .4 1 1V20c0 .6-.4 1-1 1A17 17 0 0 1 3 4c0-.6.4-1 1-1h3.5c.6 0 1 .4 1 1 0 1.3.2 2.5.6 3.6.1.3 0 .7-.2 1z"/></svg>
        0417 553 916
      </li>
      <li>
        <svg viewBox="0 0 24 24" aria-label="Email"><rect x="2" y="5" width="20" height="14" rx="2" fill="var(--gold)"/><path d="M3 6l9 7 9-7" fill="none" stroke="var(--card-cream)" stroke-width="1.6"/></svg>
        vcoph@fernmail.example
      </li>
      <li>
        <svg viewBox="0 0 24 24" aria-label="Website"><circle cx="12" cy="12" r="10" fill="var(--gold)"/><g fill="none" stroke="var(--card-cream)" stroke-width="1.3"><ellipse cx="12" cy="12" rx="4.5" ry="10"/><path d="M2 12h20M4 7h16M4 17h16"/></g></svg>
        www.velvetcrestoccasions.example.au
      </li>
    </ul>
  </section>
</body>
</html>
```